Larkspur Ridge Management - Business Cards

I need business cards. My current logo was designed by a designer at this site and I very much like and am happy with the results. I would like a business card that is trendy, unique, current yet professional. I deal with high net worth clients daily

Target Market(s)

Out of state investors looking to get into the rental market in Ohio

Industry/Entity Type

Property Management, Consulting

Contact Information for Business Card

Name, Title (Chief Financial Officer) office phone number (555) 817-3094 website address larkridgemgmt.example

Font styles to use
Sans Serif

Colors
0054AA
0677BA
7BADD7
CADEEF
E8F1F8
0094D4
00A9DD
6FCCEA
C7EBF8
E9F6FB
00AB8E
00BBA5
67D7C9
C6EFE9
E9F9F6

```html
<!DOCTYPE html>
<html lang="en">
<head>
<meta charset="utf-8">
<title>Larkspur Ridge Management – Business Cards</title>
<link rel="stylesheet" href="https://fonts.googleapis.com/css2?family=Arimo:wght@400;700&family=Montserrat:wght@800&display=swap">
<style>
  :root {
    --backdrop: #8d949a;
    --card-front: #030a28;
    --card-back-light: #1b2c58;
    --card-back-dark: #040a26;
    --accent-red: #d3222a;
    --text-white: #ffffff;
    --card-radius: 36px;
  }
  * { margin: 0; padding: 0; box-sizing: border-box; }
  html, body {
    width: 1200px;
    height: 840px;
    overflow: hidden;
    background: var(--backdrop);
    font-family: "Arimo", Arial, sans-serif;
  }
  .canvas {
    position: relative;
    width: 1200px;
    height: 840px;
  }
  .card {
    position: absolute;
    width: 533px;
    height: 305px;
    box-shadow: 0 14px 30px rgba(0, 0, 0, 0.28);
    color: var(--text-white);
  }
  .card-front {
    left: 185px;
    top: 92px;
    background: var(--card-front);
    border-radius: 0 var(--card-radius) 0 var(--card-radius);
  }
  .card-back {
    left: 490px;
    top: 421px;
    background: radial-gradient(ellipse at 15% 20%, var(--card-back-light) 0%, #12214a 45%, var(--card-back-dark) 100%);
    border-radius: var(--card-radius) 0 var(--card-radius) 0;
  }
  .contact-header {
    position: absolute;
    left: 22px;
    top: 21px;
  }
  .person-name {
    font-size: 16px;
    font-weight: 700;
    color: var(--accent-red);
    letter-spacing: 0.2px;
  }
  .person-title {
    margin-top: 3px;
    font-size: 14.5px;
    font-weight: 400;
  }
  .header-rule {
    position: absolute;
    left: 0;
    top: 66px;
    width: 166px;
    height: 1px;
    background: var(--accent-red);
  }
  .contact-list {
    position: absolute;
    left: 21px;
    top: 76px;
    list-style: none;
  }
  .contact-item {
    display: flex;
    align-items: center;
    gap: 7px;
    font-size: 14.5px;
    height: 22.5px;
  }
  .contact-icon { width: 13px; height: 13px; flex: none; }
  .brand-lockup {
    position: absolute;
    display: flex;
    align-items: center;
    gap: 10px;
    font-family: "Montserrat", Arial, sans-serif;
    font-weight: 800;
    color: var(--text-white);
    text-transform: uppercase;
    line-height: 1.05;
  }
  .brand-mark {
    flex: none;
    border-radius: 50%;
    background: var(--accent-red);
  }
  .card-front .brand-lockup {
    left: 340px;
    top: 160px;
    font-size: 20px;
  }
  .card-front .brand-mark { width: 16px; height: 16px; }
  .card-back .brand-lockup {
    left: 28px;
    top: 140px;
    font-size: 25px;
  }
  .card-back .brand-mark { width: 20px; height: 20px; }
  .website-banner {
    position: absolute;
    right: 26px;
    top: 23px;
    font-size: 13px;
    font-weight: 700;
    letter-spacing: 5px;
    white-space: nowrap;
  }
  .website-domain { color: var(--accent-red); }
</style>
</head>
<body>
<main class="canvas">

  <section class="card card-front" aria-label="Business card front">
    <header class="contact-header">
      <p class="person-name">DANA WHITFIELD</p>
      <p class="person-title">Chief Financial Officer</p>
    </header>
    <div class="header-rule"></div>
    <ul class="contact-list">
      <li class="contact-item">
        <svg class="contact-icon" viewBox="0 0 24 24" aria-hidden="true">
          <path d="M6.6 10.8a15.2 15.2 0 0 0 6.6 6.6l2.2-2.2a1 1 0 0 1 1-.25 11.4 11.4 0 0 0 3.6.57 1 1 0 0 1 1 1V20a1 1 0 0 1-1 1A17 17 0 0 1 3 4a1 1 0 0 1 1-1h3.5a1 1 0 0 1 1 1c0 1.25.2 2.45.57 3.57a1 1 0 0 1-.25 1z" fill="#d3222a"/>
          <path d="M15 3a6 6 0 0 1 6 6M15 6.5a2.5 2.5 0 0 1 2.5 2.5" stroke="#d3222a" stroke-width="1.8" fill="none" stroke-linecap="round"/>
        </svg>
        <span>(555) 817-3094</span>
      </li>
      <li class="contact-item">
        <svg class="contact-icon" viewBox="0 0 24 24" aria-hidden="true" fill="none" stroke="#d3222a" stroke-width="1.7">
          <circle cx="12" cy="12" r="10"/>
          <ellipse cx="12" cy="12" rx="4.5" ry="10"/>
          <path d="M2 12h20M4 6.5h16M4 17.5h16"/>
        </svg>
        <span>larkridgemgmt.example</span>
      </li>
    </ul>
    <div class="brand-lockup">
      <span class="brand-mark" aria-hidden="true"></span>
      <span class="brand-name">Larkspur Ridge<br>Management</span>
    </div>
  </section>

  <section class="card card-back" aria-label="Business card back">
    <p class="website-banner">www.<span class="website-domain">larkridgemgmt</span>.example</p>
    <div class="brand-lockup">
      <span class="brand-mark" aria-hidden="true"></span>
      <span class="brand-name">Larkspur Ridge<br>Management</span>
    </div>
  </section>

</main>
</body>
</html>
```